Copperleaf Motorized Shade Business Card

Hello, we've had our logo made. Now we are looking for a clean and cool looking business card. One side can just be the logo with any design elements that might look good with it. The other side will be Name, Phone Number and Email. There will not be an address on the card.

```html
<!DOCTYPE html>
<html lang="en">
<head>
<meta charset="utf-8">
<title>Copperleaf Motorized Shade – Business Card</title>
<link rel="stylesheet" href="https://fonts.googleapis.com/css2?family=Open+Sans:wght@400;600;700;800&display=swap">
<style>
  :root {
    --stage: #40434a;
    --card-yellow: #ffc20e;
    --card-yellow-light: #ffd21f;
    --card-dark: #1b1517;
    --brand-blue: #0d4a9e;
    --accent-blue: #1f8fd6;
    --ink: #1c1c1c;
    --divider: #7f8a8c;
    --ghost: #0d0a0b;
  }
  * { margin: 0; padding: 0; box-sizing: border-box; }
  html, body {
    width: 1200px; height: 840px; overflow: hidden;
    background: var(--stage);
    font-family: "Open Sans", Arial, sans-serif;
  }
  .canvas { position: relative; width: 1200px; height: 840px; }

  .card {
    position: absolute;
    width: 520px; height: 297px;
    overflow: hidden;
    box-shadow: 0 18px 40px rgba(0,0,0,.35);
  }

  /* Front */
  .card--front {
    left: 90px; top: 440px;
    background: radial-gradient(circle at 25% 25%, var(--card-yellow-light), var(--card-yellow) 70%);
    border-bottom: 7px solid var(--brand-blue);
  }
  .front-brand {
    position: absolute; left: 34px; top: 96px;
    width: 230px;
    display: flex; align-items: center; gap: 10px;
  }
  .brand-square {
    width: 28px; height: 28px; background: var(--brand-blue); flex: none;
  }
  .brand-name {
    color: var(--brand-blue);
    font-weight: 800;
    font-size: 20px; line-height: 1.1;
    white-space: nowrap;
  }
  .front-divider {
    position: absolute; left: 278px; top: 48px;
    width: 1.5px; height: 190px; background: var(--divider);
  }
  .contact {
    position: absolute; left: 304px; top: 104px;
    color: var(--ink);
  }
  .contact-name {
    color: var(--accent-blue); font-weight: 700; font-size: 22px; line-height: 1;
  }
  .contact-role { font-size: 13px; font-weight: 600; margin: 3px 0 10px; }
  .contact-line {
    display: flex; align-items: center; gap: 8px;
    font-size: 14px; font-weight: 700; margin-bottom: 4px;
  }
  .contact-line svg { width: 11px; height: 11px; flex: none; }

  /* Back */
  .card--back {
    left: 610px; top: 110px;
    background: var(--card-dark);
  }
  .back-brand {
    position: absolute; left: 110px; top: 70px;
    display: flex; align-items: center; gap: 14px;
  }
  .back-brand .brand-name { color: var(--accent-blue); font-size: 30px; }
  .back-brand .brand-square { background: var(--accent-blue); width: 40px; height: 40px; }
  .back-ghost {
    position: absolute; left: 250px; top: 150px;
    display: flex; align-items: center; gap: 18px;
    white-space: nowrap;
  }
  .back-ghost .brand-square { background: var(--ghost); width: 90px; height: 110px; }
  .back-ghost .brand-name { color: var(--ghost); font-size: 74px; }
</style>
</head>
<body>
<main class="canvas">

  <section class="card card--back" aria-label="Business card back">
    <div class="back-brand">
      <span class="brand-square"></span>
      <span class="brand-name">Copperleaf<br>Motorized Shade</span>
    </div>
    <div class="back-ghost" aria-hidden="true">
      <span class="brand-square"></span>
      <span class="brand-name">Copperleaf</span>
    </div>
  </section>

  <section class="card card--front" aria-label="Business card front">
    <div class="front-brand">
      <span class="brand-square"></span>
      <span class="brand-name">Copperleaf<br>Motorized Shade</span>
    </div>
    <div class="front-divider"></div>
    <div class="contact">
      <p class="contact-name">NAME</p>
      <p class="contact-role">Designation</p>
      <p class="contact-line">
        <svg viewBox="0 0 12 12" aria-hidden="true"><circle cx="6" cy="6" r="6" fill="#0d4a9e"/><path d="M4 3.2c.4-.3.8-.2 1 .2l.4.8c.1.3 0 .5-.2.7l-.3.3c.3.7.9 1.3 1.6 1.6l.3-.3c.2-.2.5-.3.7-.2l.8.4c.4.2.5.6.2 1-.6.8-1.5.7-2.4.2A6 6 0 0 1 3.8 5.6C3.3 4.7 3.2 3.8 4 3.2Z" fill="#fff"/></svg>
        Phone Number
      </p>
      <p class="contact-line">
        <svg viewBox="0 0 12 12" aria-hidden="true"><circle cx="6" cy="6" r="6" fill="#0d4a9e"/><rect x="3" y="4" width="6" height="4.2" rx=".5" fill="#fff"/><path d="M3.2 4.3 6 6.3l2.8-2" stroke="#0d4a9e" stroke-width=".7" fill="none"/></svg>
        Email ID
      </p>
    </div>
  </section>

</main>
</body>
</html>
```